Book Cover, Virtual Assistant book (pop art?)

I'm writing my second book ( Mastering Remote Helpers - Hand Off Chores, Keep Creating Joy) and need a cover creating.

My previous book had a pop-art cover which makes it stand out. The books aren't a set, they are for different audiences. However, I'll obviously have both on my website and it would be nice if there was some theme that ties them together.

I'd like a main image and then a wrap around the front and back of a book (even if that's just the colour and a pattern on the back and spine).

The book is all about efficiency and organisation so the cover shouldn't be over fussy or complicated, this is all about making things easier.
Updates

Hello

I wasn't very clear but in this case "Virtual Assistant" is a human, not a robot!

thanks

Target Market(s)

This book will mostly be purchased by entrepreneurs, business owners and very busy people that are thinking about working with a Virtual Assistant. They will be smart, educated but also want to be entertained a little. It needs to appeal to both men and women. I run a VA agency and this will be used as a marketing tool.

Industry/Entity Type

Business support

Font styles to use
Decorative

Requirements
Must have
• An eye catching design.
Nice to have
• Based on the title of the book Mastering Remote Helpers - Hand Off Chores, Keep Creating Joy, I have thought about the word brilliance but I'm not married to it. My last book was a pop art cover and it might be nice to keep that theme in some way but again, not married to it. I've attached my business logo. Whilst it isn't written by the business it will be used for marketing so potentially the colours or style might be incorporated in some way. Teal HEX #199BAB 25 / 155 / 171 Coral HEX #EE786E 238 / 120/ 110
Should not have
• Any old fashioned "secretary type" images or generic stock pics of phones, typewriters etc. If it's a person image it should be modern and feisty. No robots please!

```html
<!DOCTYPE html>
<html lang="en">
<head>
<meta charset="utf-8">
<title>Mastering Remote Helpers – Book Cover</title>
<link rel="stylesheet" href="https://fonts.googleapis.com/css2?family=Lato:wght@300;400;700;900&display=swap">
<style>
  :root {
    --backdrop: #e6e6e6;
    --cover-yellow: #e9c905;
    --ink: #0d0d0d;
    --accent-blue: #4a8fd8;
    --art-blue: #4f86c9;
    --art-navy: #1e1b3f;
    --band-black: #000000;
    --band-text: #ffffff;
  }

  * { margin: 0; padding: 0; box-sizing: border-box; }

  html, body {
    width: 1200px;
    height: 800px;
    overflow: hidden;
    background: var(--backdrop);
  }

  .canvas {
    position: relative;
    width: 1200px;
    height: 800px;
  }

  .book-cover {
    position: absolute;
    left: 358px;
    top: 31px;
    width: 484px;
    height: 738px;
    background: var(--cover-yellow);
    font-family: 'Lato', Arial, sans-serif;
    color: var(--ink);
    text-align: center;
    overflow: hidden;
  }

  .cover-title { font-weight: normal; }

  .title-lead {
    position: absolute;
    top: 52px;
    left: 0;
    right: 0;
    font-weight: 300;
    font-size: 46px;
    line-height: 1;
    color: var(--accent-blue);
    letter-spacing: -0.5px;
  }

  .title-main {
    position: absolute;
    top: 124px;
    left: 0;
    right: 0;
    font-weight: 900;
    font-size: 81px;
    line-height: 0.9;
    letter-spacing: -1px;
    text-transform: uppercase;
  }

  .title-main span { display: block; }

  .subtitle {
    position: absolute;
    top: 289px;
    left: 0;
    right: 0;
    font-weight: 400;
    font-size: 18px;
    line-height: 1.2;
  }

  .cover-illustration {
    position: absolute;
    left: 54px;
    top: 373px;
    width: 376px;
    height: 212px;
    border-radius: 16px;
    background:
      radial-gradient(ellipse 60% 70% at 50% 50%, var(--art-blue) 0%, #3a5f9e 45%, var(--art-navy) 100%);
  }

  .author-band {
    position: absolute;
    left: 0;
    right: 0;
    bottom: 0;
    height: 90px;
    background: var(--band-black);
    display: flex;
    align-items: center;
    justify-content: center;
  }

  .author-name {
    color: var(--band-text);
    font-weight: 700;
    font-size: 29px;
    letter-spacing: 11px;
    padding-left: 11px;
    text-transform: uppercase;
  }
</style>
</head>
<body>
  <main class="canvas">
    <article class="book-cover">
      <h1 class="cover-title">
        <span class="title-lead">Mastering</span>
        <span class="title-main"><span>Remote</span><span>Helpers</span></span>
      </h1>
      <p class="subtitle">Hand Off Chores, Keep Creating Joy</p>
      <div class="cover-illustration" role="img" aria-label="Line illustration of a helper connected by winding cables to small task icons such as a document, a paintbrush, a chat bubble, a chart and a star"></div>
      <footer class="author-band">
        <p class="author-name">Author Name</p>
      </footer>
    </article>
  </main>
</body>
</html>
```